Investment firm needs refreshed corporate powerpoint slides design

We need a new and refreshed powerpoint template for our corporate investment deck. We are a technology private equity group that primarily invests in fast growing software companies and we would like to reflect that in a modern and light blue / transparant / white powerpoint and fonts template. I have also attached our old investor deck as a guideline and also check out our website to get an idea of what we do and what type of companies we invested in. Please note that our website is old and so our presentation should be a refreshed "2017" modern design, not a copy / paste of our website design and graphics.
Updates

Target Market(s)

Investors such as high net worth individuals, pension funds, banks, financial advisors

Industry/Entity Type

Investment

Colors
33a6d7
85cae6
cfeae6
edf8f6
ffffff
fff3d1
86cfc6

Requirements
Must have
• We let you be creative, we trust you have seen more investment presentations before.
Nice to have
• Pre-built models, flow charts, graphs, charts, etc.
Should not have
• Fancy or edgy images, this has to be a modern, fresh and trustworthy looking powerpoint template. No stock images, if you do use stock images for background purposes please be creative! :-)

```html
<!DOCTYPE html>
<html lang="en">
<head>
<meta charset="utf-8">
<title>HV Growth Equity – Investor Deck Template</title>
<link rel="stylesheet" href="https://fonts.googleapis.com/css2?family=Mulish:wght@600;700;800&family=Crimson+Text:wght@400&family=Cinzel:wght@600;700&display=swap">
<style>
  :root{
    --sky-top:#c4fbfb;
    --sky-mid:#85cae6;
    --sky-deep:#33a6d7;
    --band-light:#8fd6fb;
    --band-deep:#2f8fcc;
    --navy:#1f3f76;
    --ink:#13305e;
    --teal-dark:#1b4a5e;
    --gold:#f5c531;
    --gold-soft:#f7d870;
    --cream:#fff3d1;
    --pale-blue:#a9d3f5;
    --accent-blue:#3c9be0;
    --white:#ffffff;
    --gap:#111111;
  }
  *{box-sizing:border-box;margin:0;padding:0}
  html,body{width:1053px;height:1200px;overflow:hidden;background:var(--gap)}
  .canvas{position:relative;width:1053px;height:1200px;background:var(--gap);font-family:"Mulish",sans-serif}
  .slide{position:absolute;overflow:hidden;
    background:linear-gradient(180deg,var(--sky-top) 0%,#8fdcef 40%,var(--sky-deep) 100%)}
  .brand{position:absolute;font-family:"Crimson Text",serif;font-weight:400;color:var(--ink);line-height:1}
  .deco{position:absolute;inset:0;width:100%;height:100%}

  /* cover */
  .cover{left:0;top:0;width:1053px;height:611px}
  .cover .brand{left:16px;top:2px;font-size:40px}
  .cover-title{position:absolute;left:70px;top:260px;color:var(--white);font-weight:800;font-size:49px;letter-spacing:1px}
  .cover-sub{position:absolute;left:70px;top:346px;color:var(--ink);font-weight:700;font-size:26px;letter-spacing:.6px}
  .cover-note{position:absolute;left:70px;top:393px;color:var(--ink);font-weight:700;font-size:20px;letter-spacing:.4px}

  /* small slides */
  .mini{width:518px;height:291px}
  .mini .header-band{position:absolute;left:0;top:0;width:100%;height:29px;background:var(--band-light)}
  .mini .footer-band{position:absolute;left:0;bottom:0;width:100%;height:28px;background:var(--band-deep)}
  .mini .brand{left:8px;top:3px;font-size:20px}
  .slide-heading{position:absolute;font-family:"Cinzel",serif;font-weight:700;color:var(--white);
    text-shadow:1px 1px 0 #8aa9b8,2px 2px 2px rgba(0,0,0,.25);letter-spacing:.5px;white-space:nowrap;
    border-bottom:2px solid var(--white);line-height:1}
  .swot{left:4px;top:611px}
  .location{left:530px;top:611px}
  .people{left:4px;top:908px}
  .sales{left:530px;top:908px}

  .hex-row{position:absolute;left:36px;top:68px;width:450px;height:96px}
  .swot .slide-heading{left:300px;top:183px;font-size:30px}

  .map-area{position:absolute;left:6px;top:78px;width:436px;height:134px;border-radius:26px;
    background:radial-gradient(ellipse at 55% 45%,var(--gold) 0%,#f3c93e 60%,rgba(245,197,49,.55) 100%)}
  .location .slide-heading{right:2px;top:36px;font-size:28px}

  .people .slide-heading{left:280px;top:36px;font-size:28px}
  .people-panel{position:absolute;left:61px;top:71px;width:388px;height:143px;background:var(--navy)}
  .figure{position:absolute;top:10px;width:52px;height:106px;border-radius:8px}
  .figure-label{position:absolute;top:117px;width:80px;text-align:center;color:var(--white);font-size:8.5px;font-weight:800;line-height:1.2}

  .sales .slide-heading{left:306px;top:36px;font-size:28px}
  .sales-panel{position:absolute;left:81px;top:74px;width:363px;height:155px;background:var(--cream);border:1px solid #e8d9ab}
  .sales-title{position:absolute;left:0;top:6px;width:100%;text-align:center;font-weight:800;font-size:15px;color:#1d1d1d}
  .donut{position:absolute;left:47px;top:29px}
  .legend{position:absolute;left:250px;top:52px;list-style:none}
  .legend li{font-size:13px;color:var(--navy);font-weight:600;line-height:20px;display:flex;align-items:center}
  .legend i{display:inline-block;width:7px;height:7px;margin-right:4px}
</style>
</head>
<body>
<main class="canvas">

  <!-- cover -->
  <section class="slide cover">
    <svg class="deco" viewBox="0 0 1053 611" aria-hidden="true">
      <defs>
        <linearGradient id="silver" x1="0" y1="0" x2="1" y2="1">
          <stop offset="0" stop-color="#ffffff"/>
          <stop offset=".55" stop-color="#d8d8d8"/>
          <stop offset="1" stop-color="#9a9a9a"/>
        </linearGradient>
      </defs>
      <polygon points="1053,89 768,374 1002,611 1053,611" fill="url(#silver)"/>
      <polyline points="1053,35 655,436 830,611" fill="none" stroke="#fff" stroke-width="2"/>
      <polyline points="1053,50 640,452 800,611" fill="none" stroke="#fff" stroke-width="1" opacity=".8"/>
      <polyline points="1053,20 740,340 700,375 870,611" fill="none" stroke="#fff" stroke-width="1" opacity=".6"/>
      <polyline points="1053,70 700,420 880,611" fill="none" stroke="#fff" stroke-width="1.5"/>
    </svg>
    <div class="brand">Halvern</div>
    <h1 class="cover-title">HV GROWTH EQUITY</h1>
    <p class="cover-sub">Introduction to Team and Track Record</p>
    <p class="cover-note">For US Investors</p>
  </section>

  <!-- SWOT -->
  <section class="slide mini swot">
    <div class="header-band"></div>
    <div class="footer-band"></div>
    <svg class="deco" viewBox="0 0 518 291" aria-hidden="true">
      <polygon points="518,180 470,230 518,262" fill="url(#silver)"/>
      <polyline points="518,150 395,263" fill="none" stroke="#fff" stroke-width="1"/>
      <polyline points="518,165 430,263" fill="none" stroke="#fff" stroke-width="1" opacity=".7"/>
    </svg>
    <div class="brand">Halvern</div>
    <svg class="hex-row" viewBox="0 0 450 96" aria-label="SWOT">
      <g font-family="Mulish, sans-serif" font-weight="800" font-size="50" text-anchor="middle">
        <polygon points="0,48 27,2 83,2 110,48 83,94 27,94" fill="#1b5a73"/>
        <polygon points="16,48 35,16 75,16 94,48 75,80 35,80" fill="#3aa6d8"/>
        <text x="55" y="66" fill="#fff">S</text>
        <polygon points="110,48 137,2 193,2 220,48 193,94 137,94" fill="#1b4a4a"/>
        <polygon points="126,48 145,16 185,16 204,48 185,80 145,80" fill="#dff0ee"/>
        <text x="165" y="66" fill="#fff" stroke="#1b4a4a" stroke-width="1">W</text>
        <polygon points="220,48 247,2 303,2 330,48 303,94 247,94" fill="#e3a91a"/>
        <polygon points="236,48 255,16 295,16 314,48 295,80 255,80" fill="#fff3d1"/>
        <circle cx="275" cy="48" r="19" fill="none" stroke="#fff" stroke-width="7"/>
        <polygon points="330,48 357,2 413,2 440,48 413,94 357,94" fill="#2a86b8"/>
        <polygon points="346,48 365,16 405,16 424,48 405,80 365,80" fill="#8fcaf2"/>
        <text x="385" y="66" fill="#fff">T</text>
      </g>
    </svg>
    <h2 class="slide-heading">Analysis</h2>
  </section>

  <!-- Location -->
  <section class="slide mini location">
    <div class="header-band"></div>
    <div class="footer-band"></div>
    <svg class="deco" viewBox="0 0 518 291" aria-hidden="true">
      <polygon points="518,180 470,230 518,262" fill="url(#silver)"/>
      <polyline points="518,150 395,263" fill="none" stroke="#fff" stroke-width="1"/>
    </svg>
    <div class="brand">Halvern</div>
    <div class="map-area" role="img" aria-label="World map with location pins marking office regions"></div>
    <h2 class="slide-heading">Location</h2>
  </section>

  <!-- Data analysis: people -->
  <section class="slide mini people">
    <div class="header-band"></div>
    <div class="footer-band"></div>
    <svg class="deco" viewBox="0 0 518 291" aria-hidden="true">
      <polygon points="518,180 470,230 518,262" fill="url(#silver)"/>
      <polyline points="518,150 395,263" fill="none" stroke="#fff" stroke-width="1"/>
    </svg>
    <div class="brand">Halvern</div>
    <h2 class="slide-heading">Data Analysis</h2>
    <div class="people-panel">
      <div class="figure" style="left:18px;background:linear-gradient(180deg,var(--pale-blue) 50%,var(--gold-soft) 50%)" role="img" aria-label="Person icon filled 50%"></div>
      <div class="figure-label" style="left:4px">Human 1<br>50%</div>
      <div class="figure" style="left:121px;background:linear-gradient(180deg,var(--pale-blue) 25%,var(--gold-soft) 25%)" role="img" aria-label="Person icon filled 75%"></div>
      <div class="figure-label" style="left:107px">Human 2<br>75%</div>
      <div class="figure" style="left:215px;background:linear-gradient(180deg,var(--pale-blue) 75%,var(--gold-soft) 75%)" role="img" aria-label="Person icon filled 25%"></div>
      <div class="figure-label" style="left:201px">Human 3<br>25%</div>
      <div class="figure" style="left:318px;background:linear-gradient(180deg,var(--pale-blue) 5%,var(--gold) 5%)" role="img" aria-label="Person icon filled 95%"></div>
      <div class="figure-label" style="left:304px">Human 1<br>95%</div>
    </div>
  </section>

  <!-- Data analysis: sales -->
  <section class="slide mini sales">
    <div class="header-band"></div>
    <div class="footer-band"></div>
    <svg class="deco" viewBox="0 0 518 291" aria-hidden="true">
      <polygon points="518,180 470,230 518,262" fill="url(#silver)"/>
      <polyline points="518,150 395,263" fill="none" stroke="#fff" stroke-width="1"/>
    </svg>
    <div class="brand">Halvern</div>
    <h2 class="slide-heading">Data Analysis</h2>
    <div class="sales-panel">
      <div class="sales-title">Sales</div>
      <svg class="donut" width="104" height="104" viewBox="0 0 104 104" aria-label="Sales donut chart">
        <g transform="rotate(-90 52 52)" fill="none" stroke-width="12">
          <circle cx="52" cy="52" r="44" stroke="var(--navy)" stroke-dasharray="162 115"/>
          <circle cx="52" cy="52" r="44" stroke="var(--gold-soft)" stroke-dasharray="63.2 213.3" stroke-dashoffset="-162"/>
          <circle cx="52" cy="52" r="44" stroke="var(--teal-dark)" stroke-dasharray="27.6 248.9" stroke-dashoffset="-225.2"/>
          <circle cx="52" cy="52" r="44" stroke="var(--accent-blue)" stroke-dasharray="23.7 252.8" stroke-dashoffset="-252.8"/>
        </g>
        <g font-family="Mulish, sans-serif" font-size="6" font-weight="700" fill="#fff" text-anchor="middle">
          <text x="96" y="54">8.2</text>
          <text x="8" y="54" fill="#8a7a40">3.2</text>
          <text x="20" y="22">1.4</text>
          <text x="44" y="10">1.2</text>
        </g>
      </svg>
      <ul class="legend">
        <li><i style="background:var(--navy)"></i>Investor</li>
        <li><i style="background:var(--gold-soft)"></i>Finance</li>
        <li><i style="background:var(--teal-dark)"></i>Office</li>
        <li><i style="background:var(--accent-blue)"></i>Manager</li>
      </ul>
    </div>
  </section>

</main>
</body>
</html>
```